We require a business card that promotes our Electrical business. Things we would like included are;
1) our business name, Bright Path Electrical and Communication
2) Our Electrical licence, EC 73620
3) Our ABN, 41 297 506 183
4) Our website, www.korvanelectric.com.au
5) Our Email, info@korvanelectric.com.au
6) Our contact number, 0462 158 704
7) Our address, 57 Larkfield Rd West Dunmore Perth 6109
8) Our logo, I will attach this (can you please change it so the ackground is white not black)
9) Our colours are red and white and perhaps some black
10) Managing Director Tomasz Relhuvan
11) the back to say 'notes' and have some lines for writing

Target Market(s)

General

Industry/Entity Type

Electrical

Contact Information for Business Card

Include the colour white, black and red.

Font styles to use
Sans Serif

Requirements
Nice to have
• A thunder bolt or a power point or a cord or something electrical, cartoon image of a cartoon like electrical tradie

```html
<!DOCTYPE html>
<html lang="en">
<head>
<meta charset="utf-8">
<title>Bright Path Electrical and Communication – Business Card</title>
<link rel="stylesheet" href="https://fonts.googleapis.com/css2?family=Lato:wght@400;700;900&family=Montserrat:wght@800&display=swap">
<style>
  :root {
    --red: #e5202a;
    --black: #111111;
    --white: #ffffff;
    --ink: #1c1c1c;
    --rule: #d4d4d4;
    --faint: #e6e6e6;
    --backdrop: #e8e9ea;
  }
  * { margin: 0; padding: 0; box-sizing: border-box; }
  html, body { width: 1200px; height: 900px; overflow: hidden; }
  body {
    background: var(--backdrop);
    font-family: "Lato", Arial, sans-serif;
    color: var(--ink);
    position: relative;
  }
  .card {
    position: absolute;
    top: 296px;
    width: 540px;
    height: 309px;
    background: var(--white);
    overflow: hidden;
    box-shadow: 0 6px 18px rgba(0,0,0,0.12);
  }
  .card--front { left: 620px; }
  .card--back { left: 40px; }

  .band-art { position: absolute; left: 0; bottom: 0; width: 540px; height: 30px; }

  /* front */
  .brand {
    position: absolute;
    left: 34px;
    top: 148px;
    display: flex;
    align-items: center;
    gap: 14px;
  }
  .brand__dot {
    width: 34px; height: 34px;
    border-radius: 50%;
    background: var(--red);
    flex: none;
  }
  .brand__name {
    font-weight: 900;
    font-size: 19px;
    line-height: 1.15;
    color: var(--black);
    width: 190px;
  }
  .contact {
    position: absolute;
    left: 292px;
    top: 36px;
    font-size: 12px;
    line-height: 1.45;
  }
  .contact__name { font-size: 18px; font-weight: 900; margin-bottom: 3px; }
  .contact__surname { color: var(--red); }
  .contact__group + .contact__group { margin-top: 13px; }

  /* back */
  .notes-lines { position: absolute; inset: 0 0 12px 0; }
  .notes-watermark {
    position: absolute;
    left: 0; right: 0;
    top: 128px;
    text-align: center;
    font-weight: 900;
    font-size: 24px;
    line-height: 1.2;
    color: var(--faint);
  }
  .notes-title {
    position: absolute;
    left: 130px; top: 28px;
    padding: 0 8px;
    background: var(--white);
    font-family: "Montserrat", Arial, sans-serif;
    font-weight: 800;
    font-size: 26px;
    letter-spacing: 3px;
    color: var(--red);
  }
</style>
</head>
<body>

  <section class="card card--back" aria-label="Card back">
    <svg class="notes-lines" width="540" height="297" viewBox="0 0 540 297" aria-hidden="true">
      <g stroke="var(--rule)" stroke-width="1.2">
        <line x1="0" y1="22" x2="540" y2="22"/>
        <line x1="0" y1="48" x2="540" y2="48"/>
        <line x1="0" y1="74" x2="540" y2="74"/>
        <line x1="0" y1="100" x2="540" y2="100"/>
        <line x1="0" y1="126" x2="540" y2="126"/>
        <line x1="0" y1="152" x2="540" y2="152"/>
        <line x1="0" y1="178" x2="540" y2="178"/>
        <line x1="0" y1="204" x2="540" y2="204"/>
        <line x1="0" y1="230" x2="540" y2="230"/>
        <line x1="0" y1="256" x2="540" y2="256"/>
        <line x1="0" y1="282" x2="540" y2="282"/>
      </g>
    </svg>
    <p class="notes-watermark" aria-hidden="true">Bright Path Electrical<br>and Communication</p>
    <h2 class="notes-title">Notes</h2>
    <svg class="band-art" viewBox="0 0 540 30" aria-hidden="true">
      <rect x="0" y="17" width="540" height="13" fill="var(--red)"/>
    </svg>
  </section>

  <section class="card card--front" aria-label="Card front">
    <div class="brand">
      <span class="brand__dot" aria-hidden="true"></span>
      <span class="brand__name">Bright Path Electrical and Communication</span>
    </div>

    <div class="contact">
      <p class="contact__name">Tomasz <span class="contact__surname">Relhuvan</span></p>
      <div class="contact__group">
        <p>Electrical licence, EC 73620</p>
        <p>ABN, 41 297 506 183</p>
      </div>
      <div class="contact__group">
        <p>0462 158 704</p>
        <p>www.korvanelectric.com.au</p>
        <p>info@korvanelectric.com.au</p>
      </div>
      <div class="contact__group">
        <p>57 Larkfield Rd West</p>
        <p>Dunmore Perth 6109</p>
      </div>
    </div>

    <svg class="band-art" viewBox="0 0 540 30" aria-hidden="true">
      <polygon points="322,3 540,3 540,17 306,17" fill="var(--black)"/>
      <rect x="0" y="17" width="540" height="13" fill="var(--red)"/>
    </svg>
  </section>

</body>
</html>
```